Whitmore Business Card Design

The name of the business is Dara Whitmore, CPA LLC
The service that we offer is Accounting, Tax & Consulting Services. I need it to have the following items:
Dara Whitmore, Principal
Phone Number
Email Address
Physical Address

I have attached the company logo, one in black and one in white. Please provide a design in black background and the other in white background. Please include "Accounting, Tax & Consulting Services". I want the business card to be clean and very professional.

```html
<!DOCTYPE html>
<html lang="en">
<head>
<meta charset="utf-8">
<title>Dara Whitmore, CPA LLC — Business Cards</title>
<link rel="stylesheet" href="https://fonts.googleapis.com/css2?family=Lato:wght@400&family=Montserrat:wght@500;600&family=Archivo+Black&display=swap">
<style>
  :root {
    --backdrop: #b8b8b8;
    --paper: #ffffff;
    --charcoal: #3a3a3c;
    --ink: #404042;
    --crimson: #9b1b1f;
    --muted: #808082;
    --shadow: rgba(0,0,0,0.55);
  }
  * { margin: 0; padding: 0; box-sizing: border-box; }
  html, body { width: 1075px; height: 1200px; overflow: hidden; }
  body { background: var(--backdrop); position: relative; font-family: "Lato", sans-serif; }

  .card {
    position: absolute; left: 206px; width: 663px; height: 395px;
    box-shadow: 3px 3px 3px var(--shadow);
    overflow: hidden;
  }
  .card--front { top: 187px; background: var(--paper); }
  .card--back { top: 637px; background: var(--charcoal); }

  .brand { position: absolute; text-align: center; }
  .brand__mark { width: 34px; height: 34px; background: var(--crimson); margin: 0 auto 14px; }
  .brand__name { font-family: "Montserrat", sans-serif; font-weight: 600; font-size: 23px; letter-spacing: 0.5px; white-space: nowrap; }
  .brand__tagline { font-family: "Montserrat", sans-serif; font-weight: 500; font-size: 16px; letter-spacing: 2.4px; color: var(--muted); margin-top: 3px; white-space: nowrap; }

  .card--front .brand { left: 288px; width: 336px; top: 100px; }
  .card--front .brand__name { color: var(--ink); }

  .person { position: absolute; left: 32px; top: 218px; }
  .person__name { font-size: 24px; color: var(--ink); line-height: 1; }
  .person__name .first { color: var(--crimson); }
  .person__role { font-size: 18px; color: var(--ink); margin-top: 5px; }
  .person__rule { position: absolute; left: 32px; top: 275px; width: 196px; height: 4px; background: var(--crimson); }

  .contact-band { position: absolute; left: 0; top: 279px; width: 100%; height: 116px; background: var(--charcoal); color: #fff; font-size: 18.5px; }
  .contact-list { position: absolute; left: 32px; top: 32px; list-style: none; line-height: 24px; }
  .contact-list li { display: flex; align-items: center; gap: 6px; }
  .contact-list svg { width: 17px; height: 14px; fill: var(--crimson); }
  .address { position: absolute; right: 42px; top: 31px; text-align: right; line-height: 24px; font-style: normal; }

  .card--back .brand { left: 0; width: 100%; top: 175px; }
  .card--back .brand__mark { margin-bottom: 16px; }
  .card--back .brand__name { color: #fff; font-size: 26px; }
  .card--back .brand__tagline { font-size: 18px; letter-spacing: 2.6px; color: #8a8a8c; }

  .services-band { position: absolute; left: 0; bottom: 0; width: 100%; height: 45px; background: var(--crimson); color: #fff; font-family: "Archivo Black", sans-serif; font-size: 17.5px; letter-spacing: 1.3px; text-align: center; line-height: 46px; }
</style>
</head>
<body>
  <section class="card card--front">
    <div class="brand">
      <div class="brand__mark"></div>
      <div class="brand__name">DARA WHITMORE, CPA LLC</div>
      <div class="brand__tagline">CERTIFIED PUBLIC ACCOUNTANT</div>
    </div>
    <div class="person">
      <div class="person__name"><span class="first">DARA</span> WHITMORE</div>
      <div class="person__role">Principal</div>
    </div>
    <div class="person__rule"></div>
    <div class="contact-band">
      <ul class="contact-list">
        <li><svg viewBox="0 0 24 24" aria-hidden="true"><path d="M6.6 10.8a15.1 15.1 0 006.6 6.6l2.2-2.2c.3-.3.7-.4 1-.2 1.1.4 2.3.6 3.6.6.6 0 1 .4 1 1V20c0 .6-.4 1-1 1C10.6 21 3 13.4 3 4c0-.6.4-1 1-1h3.5c.6 0 1 .4 1 1 0 1.3.2 2.5.6 3.6.1.3 0 .7-.2 1z"/></svg>044-123 456 789</li>
        <li><svg viewBox="0 0 24 18" aria-hidden="true"><path d="M0 0h24v18H0z M2 2l10 7 10-7" /></svg>info@whitmorecpa.com</li>
      </ul>
      <address class="address">421, Address line goes here<br>45452,Country Name</address>
    </div>
  </section>

  <section class="card card--back">
    <div class="brand">
      <div class="brand__mark"></div>
      <div class="brand__name">DARA WHITMORE, CPA LLC</div>
      <div class="brand__tagline">CERTIFIED PUBLIC ACCOUNTANT</div>
    </div>
    <div class="services-band">ACCOUNTING, TAX &amp; CONSULTING SERVICES</div>
  </section>
</body>
</html>
```